Business Card Design - Law Firm

We are a boutique law firm located near the beach in Manly, Australia. We have recently had a new logo designed and are revamping our business cards with the new logo.

We have recently had a business card design done for us but are not entirely happy with it. We are looking for something modern, simplistic but striking. We would like to see multiple designs.

We have attached a word document which includes our new logo and the current business card design which we are looking at moving away from.

We would like the business cards to be double sided. We would like the design to include something which we can print in gloss colour when we send it to the business card printers.

```html
<!DOCTYPE html>
<html lang="en">
<head>
<meta charset="utf-8">
<title>Harbourne &amp; Partners – Business Card</title>
<link rel="stylesheet" href="https://fonts.googleapis.com/css2?family=Lato:wght@400;700&display=swap">
<style>
  :root {
    --backdrop-light: #e4e5e6;
    --backdrop-dark: #8b8d8f;
    --gold: #c9b24f;
    --blue-top: #3f78e0;
    --blue-bottom: #4b9bd6;
    --white: #ffffff;
    --ink: #16191d;
    --teal-top: #3bb5d3;
    --teal-bottom: #46dad2;
    --mark-blue: #2f4fd8;
  }
  * { margin: 0; padding: 0; box-sizing: border-box; }
  html, body { width: 1200px; height: 1000px; overflow: hidden; }
  body {
    position: relative;
    background: radial-gradient(ellipse at 50% 50%, var(--backdrop-light) 0%, #c4c5c7 55%, var(--backdrop-dark) 100%);
    font-family: "Lato", Arial, sans-serif;
    color: var(--ink);
  }
  .card { position: absolute; left: 206px; width: 787px; height: 472px; overflow: hidden; }
  .card-front { top: 23px; }
  .card-back { top: 508px; background: var(--white); }

  .front-shape { position: absolute; inset: 0; }
  .front-brand {
    position: absolute; left: 0; width: 787px; top: 300px;
    display: flex; align-items: center; justify-content: center; gap: 16px;
  }
  .brand-dot { width: 22px; height: 22px; border-radius: 50%; background: var(--mark-blue); flex: none; }
  .brand-name {
    font-weight: 700; font-size: 38px; letter-spacing: 2px; color: var(--ink); white-space: nowrap;
  }

  .person-name { position: absolute; left: 59px; top: 66px; font-size: 50px; font-weight: 400; letter-spacing: -0.5px; white-space: nowrap; }
  .person-role { position: absolute; left: 67px; top: 126px; font-size: 34px; font-weight: 400; white-space: nowrap; }
  .back-brand {
    position: absolute; left: 480px; top: 160px; width: 260px;
    display: flex; align-items: center; justify-content: center; gap: 10px;
  }
  .back-brand .brand-dot { width: 14px; height: 14px; }
  .back-brand .brand-name { font-size: 20px; letter-spacing: 1px; }

  .gold-band { position: absolute; left: 0; top: 244px; width: 100%; height: 20px; background: var(--gold); }
  .contact-panel {
    position: absolute; left: 0; top: 264px; width: 100%; height: 208px;
    background: linear-gradient(180deg, var(--teal-top), var(--teal-bottom));
  }
  .contact-list { position: absolute; left: 66px; top: 22px; list-style: none; }
  .contact-list li { display: flex; height: 32.5px; align-items: center; font-size: 20px; white-space: nowrap; }
  .contact-label { width: 106px; font-weight: 700; }
  .contact-value { font-weight: 400; }
</style>
</head>
<body>
  <section class="card card-front" aria-label="Card front">
    <svg class="front-shape" width="787" height="472" viewBox="0 0 787 472">
      <defs>
        <linearGradient id="blueSide" x1="0" y1="0" x2="0" y2="1">
          <stop offset="0" stop-color="#3f78e0"/>
          <stop offset="1" stop-color="#4b9bd6"/>
        </linearGradient>
        <filter id="softShadow" x="-10%" y="-10%" width="120%" height="120%">
          <feDropShadow dx="0" dy="0" stdDeviation="7" flood-color="#000" flood-opacity="0.45"/>
        </filter>
      </defs>
      <rect x="0" y="0" width="394" height="472" fill="#c9b24f"/>
      <rect x="394" y="0" width="393" height="472" fill="url(#blueSide)"/>
      <path filter="url(#softShadow)" fill="#ffffff"
        d="M230 0 C150 40 95 160 86 300 C82 380 90 440 100 472 L580 472 C640 400 690 320 686 210 C683 120 665 50 650 0 Z"/>
    </svg>
    <div class="front-brand">
      <span class="brand-dot"></span>
      <span class="brand-name">Harbourne &amp; Partners</span>
    </div>
  </section>

  <section class="card card-back" aria-label="Card back">
    <h1 class="person-name">Elise Marlow</h1>
    <p class="person-role">Practice Manager</p>
    <div class="back-brand">
      <span class="brand-dot"></span>
      <span class="brand-name">Harbourne &amp; Partners</span>
    </div>
    <div class="gold-band"></div>
    <div class="contact-panel">
      <ul class="contact-list">
        <li><span class="contact-label">Phone:</span><span class="contact-value">(02) 0955 3140</span></li>
        <li><span class="contact-label">Email :</span><span class="contact-value">elise.marlow@harbournelaw.com.au</span></li>
        <li><span class="contact-label">Website:</span><span class="contact-value">www.harbourneandpartners.com.au</span></li>
        <li><span class="contact-label">Address:</span><span class="contact-value">Suite 4, 12 Tidewater Lane COVEBAY NSW 2483</span></li>
      </ul>
    </div>
  </section>
</body>
</html>
```